The Corvane Agency

We are a pr, social media and strategy agency specializing in the pet industry. We would like a new dynamic design of our existing website. We think it is currently outdated and looks too corporate. We would like it to look more consumer oriented as we primarily market pet products. We would like warm imagery involving pets and while pets are fun, this is still a business website and needs to maintain a professional look. We are hired by business owners and executives.
I would like some of our work featured on the home page.
Our primary service tabs are:
Public Relations
Social Media
Product Consulting
Most of the content will remain the same but we are open to suggestions!
Our current website can be found at www.corvanepetpr.example.
We are open to other colors than in our logo and on our current page.
This is a design only project and will not require programming. The selected designer will need to provide at least one interior page in addition to the home page.

Industry/Entity Type

Pet

Requirements
Should not have
• Cartoon type figures. Pet puns.

```html
<!DOCTYPE html>
<html lang="en">
<head>
<meta charset="utf-8">
<title>The Corvane Agency</title>
<link href="https://fonts.googleapis.com/css2?family=Lato:wght@300;400;700&display=swap" rel="stylesheet">
<style>
:root{
  --red:#e3232b;
  --orange:#f26b2a;
  --orange-soft:#f58a4a;
  --ink:#2b2b2b;
  --grey:#6a6a6a;
  --light-grey:#9a9a9a;
  --panel:#e9e9e9;
  --link:#1e7aa8;
  --bg:#f6f7f3;
}
*{margin:0;padding:0;box-sizing:border-box}
html,body{width:1200px;height:1200px;overflow:hidden}
body{font-family:'Lato',sans-serif;color:var(--ink);background:radial-gradient(ellipse at 50% 20%,#ffffff 0%,var(--bg) 70%);position:relative}
.abs{position:absolute}
.social{top:14px;left:921px;display:flex;gap:5px}
.social span{width:22px;height:22px;border-radius:50%;background:var(--orange);display:block}
.brand{color:var(--red);font-weight:400;font-size:25px;letter-spacing:-0.5px;display:flex;align-items:center;gap:4px;line-height:1}
.brand i{width:6px;height:6px;border-radius:50%;background:var(--orange);display:block}
.brand-top{top:56px;left:200px}
.nav{top:60px;left:434px;width:566px;height:32px;border-bottom:1px dotted #b9b9b9;display:flex;align-items:center;gap:19px;font-size:11.5px;color:var(--ink);padding-bottom:4px}
.nav svg{margin-right:-2px}
.hero-photo{top:92px;left:200px;width:464px;height:304px;background:radial-gradient(ellipse at 35% 55%,#b3283c 0%,#c94a5a 25%,#e6e1dc 55%,rgba(246,247,243,0) 78%);border-radius:40% 45% 10% 20%}
.hero-title{top:146px;left:686px;font-size:74px;font-weight:700;color:var(--red);letter-spacing:-4px;line-height:1}
.hero-sub{top:214px;left:689px;font-size:44px;font-weight:400;color:var(--orange);letter-spacing:-1.5px;line-height:1}
.hero-text{top:274px;left:690px;width:320px;font-size:11px;line-height:13.6px}
.hero-more{top:324px;left:690px;font-size:11.5px;font-weight:700;display:flex;align-items:center;gap:2px}
.hero-more i{width:16px;height:16px;border-radius:50%;background:var(--orange);display:flex;align-items:center;justify-content:center}
.dots{top:382px;left:550px;display:flex;gap:7px}
.dots span{width:9px;height:9px;border-radius:50%;background:var(--orange)}
.about{top:402px;left:200px;width:802px;height:106px;background:var(--panel);border-radius:6px;box-shadow:0 2px 0 #cfcfcf;display:flex}
.about-tab{width:96px;background:linear-gradient(160deg,var(--orange) 0%,#f58a4a 100%);border-radius:6px 0 0 6px;color:#fff;font-weight:700;font-size:16px;letter-spacing:-1px;display:flex;align-items:center;justify-content:center;border-right:3px solid #d6d6d6}
.about-text{padding:20px 24px 0 20px;font-size:13px;font-weight:300;line-height:16.5px;color:var(--grey)}
.section-head{display:flex;align-items:center;gap:10px;color:var(--red);font-size:22px;letter-spacing:-1px;font-weight:400}
.head-testi{top:530px;left:199px}
.card{top:581px;width:252px;height:80px;background:#fff;border-radius:6px;box-shadow:0 1px 3px rgba(0,0,0,.15);padding:8px 10px 0 10px}
.card p{font-size:10.5px;font-weight:300;line-height:13.5px;color:var(--grey);padding-left:12px;position:relative}
.card p b{font-weight:700;color:var(--ink);font-size:14px;position:absolute;left:0;top:-3px}
.card p em{font-style:normal;font-weight:700;color:var(--ink);font-size:13px;margin-left:4px}
.card .foot{display:flex;justify-content:space-between;margin-top:5px;font-size:11px}
.card .who{color:var(--orange);font-weight:700}
.card .more{color:var(--grey);font-size:10px;margin-right:16px}
.head-team{top:692px;left:199px}
.team-text{top:737px;left:202px;width:800px;font-size:13px;font-weight:300;line-height:17px;color:var(--grey)}
.member{top:798px;width:150px;text-align:center}
.portrait{width:132px;height:132px;margin:0 auto;border-radius:50%;border:3px solid var(--orange);box-shadow:0 8px 6px -4px rgba(0,0,0,.15)}
.member .name{margin-top:26px;font-size:11px;color:var(--ink)}
.member .role{font-size:11px;color:var(--link);margin-top:1px}
.rule{left:0;width:1200px;border-top:1px dotted #bcbcbc}
.head-blog{top:1034px;left:199px}
.blog-links{top:1085px;left:236px;display:flex;gap:10px;font-size:11px}
.blog-links a{color:var(--link);text-decoration:underline;display:flex;align-items:center;gap:3px}
.blog-links a i{width:7px;height:7px;border-radius:50%;background:var(--orange);display:block}
.foot-nav{top:1140px;left:200px;display:flex;gap:37px;font-size:11px;color:var(--grey)}
.foot-copy{top:1163px;left:200px;font-size:10.5px;font-weight:300;line-height:13.5px;color:var(--grey)}
.brand-foot{top:1150px;left:878px}
</style>
</head>
<body>

<div class="abs social" aria-label="Social links"><span aria-label="Social profile"></span><span aria-label="Social profile"></span><span aria-label="News feed"></span></div>

<div class="abs brand brand-top"><i></i>Corvane Agency</div>

<nav class="abs nav">
  <svg width="24" height="22" viewBox="0 0 24 22" aria-label="Home"><path d="M12 1 L23 11 H20 V21 H14 V14 H10 V21 H4 V11 H1 Z" fill="#f26b2a"/></svg>
  <span>PR</span><span>SOCAIL MEDIA</span><span>PET EXPERTS</span><span>BUSINESS DEVELOPMENT</span><span>CASE STUDIES</span><span>OUR TEAM</span>
</nav>

<div class="abs hero-photo" role="img" aria-label="Photo of a shaggy dog wrapped in a red towel beside a white long-haired cat"></div>
<div class="abs hero-title">Redefining</div>
<div class="abs hero-sub">pet products</div>
<p class="abs hero-text">The Corvane Agency Knows what it takes to successfully market your pet product, whether it's a new product or arebrand, and expand your target audience.</p>
<div class="abs hero-more">READMORE <i><svg width="6" height="8" viewBox="0 0 6 8"><path d="M0 0 L6 4 L0 8Z" fill="#fff"/></svg></i></div>
<div class="abs dots"><span></span><span></span><span></span></div>

<section class="abs about">
  <div class="about-tab">ABOUT US</div>
  <p class="about-text">PR has evolved from public relations to personal relations. As new communication tools have emerged, old habits have been buried, giving way to the consumer revolution of social media. At Corvane, we tap the best ways to connect you with those in the pet industry. That focus makes our team your ideal partner for creating a community as faithful as a favorite pet.</p>
</section>

<h2 class="abs section-head head-testi">
  <svg width="38" height="36" viewBox="0 0 38 36" aria-hidden="true"><path d="M19 2C9 2 1 8.5 1 16.5c0 4.5 2.5 8.4 6.5 11L5 34l9-4.5c1.6.4 3.3.6 5 .6 10 0 18-6.5 18-14.6S29 2 19 2z" fill="#c9c9c9"/><circle cx="11" cy="16" r="2.6" fill="#fff"/><circle cx="19" cy="16" r="2.6" fill="#fff"/><circle cx="27" cy="16" r="2.6" fill="#fff"/></svg>
  TESTIMONIALS
</h2>

<div class="abs card" style="left:200px"><p><b>“</b>I've had the opportunity to work with Corvane team members and can assure you they are professional<em>”</em></p><div class="foot"><span class="who">- Rob Calden, President</span><span class="more">READMORE</span></div></div>
<div class="abs card" style="left:474px"><p><b>“</b>I've had the opportunity to work with Corvane team members and can assure you they are professional<em>”</em></p><div class="foot"><span class="who">- Rob Calden, President</span><span class="more">READMORE</span></div></div>
<div class="abs card" style="left:746px"><p><b>“</b>I've had the opportunity to work with Corvane team members and can assure you they are professional<em>”</em></p><div class="foot"><span class="who">- Rob Calden, President</span><span class="more">READMORE</span></div></div>

<h2 class="abs section-head head-team">
  <svg width="46" height="36" viewBox="0 0 46 36" aria-hidden="true"><circle cx="30" cy="9" r="7" fill="#c9c9c9"/><path d="M16 36c0-9 6-15 14-15s14 6 14 15z" fill="#c9c9c9"/><circle cx="15" cy="12" r="6" fill="#d8d8d8"/><path d="M2 36c0-8 5-13 13-13 3 0 5 .8 7 2-3 3-5 7-5 11z" fill="#d8d8d8"/></svg>
  OUR TEAM
</h2>
<p class="abs team-text">Teamwork is just that...a true “team” committed to real “work.” It takes a collaborative spirit and willingness to not only excel in our individual roles, but also elevate the work of those around us.</p>

<div class="abs member" style="left:205px"><div class="portrait" role="img" aria-label="Portrait of Sienna Marlow" style="background:radial-gradient(circle at 50% 40%,#e9c98a,#3a2e28 75%)"></div><div class="name">SIENNA MARLOW</div><div class="role">PRINCIPAL</div></div>
<div class="abs member" style="left:366px"><div class="portrait" role="img" aria-label="Portrait of Clara Desmet" style="background:radial-gradient(circle at 50% 40%,#e8c6b2,#4a3028 75%)"></div><div class="name">CLARA DESMET</div><div class="role">MANAGING DIRECTOR</div></div>
<div class="abs member" style="left:526px"><div class="portrait" role="img" aria-label="Portrait of Owen Tallis" style="background:radial-gradient(circle at 50% 45%,#2a2a2a,#f4f4f4 70%)"></div><div class="name">OWEN TALLIS</div><div class="role">SOCIAL MEDIA MANAGER</div></div>
<div class="abs member" style="left:687px"><div class="portrait" role="img" aria-label="Portrait of Brooke Hadley" style="background:radial-gradient(circle at 50% 40%,#e6c2ae,#5a3a2c 75%)"></div><div class="name">BROOKE HADLEY</div><div class="role">ACCOUNT COORDINATOR</div></div>
<div class="abs member" style="left:847px"><div class="portrait" role="img" aria-label="Portrait of Nora Whitfield" style="background:radial-gradient(circle at 50% 40%,#edd2bf,#a27c5e 75%)"></div><div class="name">NORA WHITFIELD</div><div class="role">PET DIVISION MANAGER</div></div>

<div class="abs rule" style="top:1012px"></div>

<h2 class="abs section-head head-blog" style="font-size:23px">
  <svg width="36" height="36" viewBox="0 0 36 36" aria-hidden="true"><rect width="36" height="36" rx="6" fill="#c9c9c9"/><circle cx="10" cy="26" r="3.5" fill="#fff"/><path d="M7 15a14 14 0 0 1 14 14" stroke="#fff" stroke-width="4" fill="none"/><path d="M7 7a22 22 0 0 1 22 22" stroke="#fff" stroke-width="4" fill="none"/></svg>
  MOST RECENT BLOG POSTS
</h2>
<div class="abs blog-links">
  <a href="#"><i></i>Trailpaw Featured on Morning Desk</a>
  <a href="#"><i></i>The Power of Stress</a>
  <a href="#"><i></i>The Evolution of the Ideas: Brainstorming</a>
  <a href="#"><i></i>Can Giving Go Viral?</a>
  <a href="#"><i></i>Relationship Building</a>
</div>

<div class="abs rule" style="top:1124px"></div>

<div class="abs foot-nav"><span>CONTACT</span><span>CAREERS</span><span>LOVE LIST</span><span>BLOG</span><span>SITE MAP</span></div>
<p class="abs foot-copy">©2014 The Corvane Agency | 418 Juniper Ridge Rd. NV 89500 | 775.555.0148<br>social.example/thecorvaneagency</p>
<div class="abs brand brand-foot"><i></i>Corvane Agency</div>

</body>
</html>
```